PIKEmoor box Graphic design on existing box dye cut.

we are a flooring company and we are making a sample box. the logo and information that need to be on the box is already established. we just need someone to lay it out on the box "DYE_CUT" . PLEASE CHANGE DASHES ON LOOK TOUCH PICK TO DOTS AND REMOVE THE EXCLAMATION POINT ALSO, please give me a lighter version of the logo...it appears a bit dark on the box. perhaps lighten a bit. .so we need to work with someone who understands how to work with a box dye cut. We want to wrap the logo around the entire 4 sides of the box and leave the top and bottom a black color. The inside of the box will have a similar photo with bullet points (be creative how to include them). I have enclosed a picture of this how it should read. Also, the large inside flap will have a specification sheet. I have included photos of this sheet for your reference… all spec information needs to be included as written. We need to include a QR code on this inside flap which will later allow architects to download the spec.The very front cover that we submitted with the PIKEMOOR look touch pick…I would like a few reeditions of the font on this as I am not completely sold on the font. I am including pictures of how it should look, from a cut and paste model I made.

Target Market(s)

architects and designers

Industry/Entity Type

Architecture

Colors
474747

Requirements
Must have
• Graphic designer MUST know how to work with dye cuts provided and scale artwork to work on dye cut sizes provided. must look professional and elegant this is for architects and designers
Nice to have
• box must look good from all sides . short and long sides. pikemoor photo needs to be on all 4 sides...

```html
<!DOCTYPE html>
<html lang="en">
<head>
<meta charset="utf-8">
<title>PIKEMOOR sample box dieline</title>
<link rel="stylesheet" href="https://fonts.googleapis.com/css2?family=Montserrat:wght@600;800&display=swap">
<style>
  :root {
    --paper: #ffffff;
    --wood-light: #e6e6e6;
    --wood-mid: #cfcfcf;
    --wood-dark: #b4b4b4;
    --cut-line: #111111;
    --crease-line: #e0262b;
    --ink: #1c1c1c;
    --label: rgba(255, 255, 255, 0.82);
    --rule: #9a9a9a;
    --caption: #6a6a6a;
  }
  html, body {
    margin: 0;
    padding: 0;
    width: 1125px;
    height: 1200px;
    overflow: hidden;
    background: var(--paper);
  }
  .dieline {
    display: block;
    width: 1125px;
    height: 1200px;
  }
  .wood { fill: url(#woodTone); }
  .cut { fill: none; stroke: var(--cut-line); stroke-width: 1.4; stroke-linejoin: round; }
  .crease { fill: none; stroke: var(--crease-line); stroke-width: 1.1; }
  .brand-name {
    font-family: "Montserrat", sans-serif;
    font-weight: 800;
    font-size: 24px;
    fill: var(--ink);
    text-anchor: middle;
    letter-spacing: 0.5px;
  }
  .brand-tag {
    font-family: "Montserrat", sans-serif;
    font-weight: 800;
    font-size: 10.5px;
    fill: var(--ink);
    text-anchor: middle;
    letter-spacing: 1.6px;
  }
  .label-name { font-size: 15px; }
  .label-tag { font-size: 6.5px; letter-spacing: 1px; }
  .label-caption {
    font-family: "Montserrat", sans-serif;
    font-weight: 600;
    font-size: 5.5px;
    fill: var(--caption);
    text-anchor: middle;
    letter-spacing: 0.6px;
  }
  .label-panel { fill: var(--label); }
  .spec-rule { stroke: var(--rule); stroke-width: 0.8; fill: none; }
</style>
</head>
<body>
<svg class="dieline" viewBox="0 0 1200 1280" xmlns="http://www.w3.org/2000/svg">
  <defs>
    <linearGradient id="woodTone" x1="0" y1="0" x2="0" y2="1">
      <stop offset="0" stop-color="#e6e6e6"/>
      <stop offset="0.35" stop-color="#cfcfcf"/>
      <stop offset="0.6" stop-color="#e6e6e6"/>
      <stop offset="0.85" stop-color="#b4b4b4"/>
      <stop offset="1" stop-color="#cfcfcf"/>
    </linearGradient>
  </defs>

  <g class="sheet-surface" role="img" aria-label="Grey weathered wood plank photograph across the box sheet">
    <rect class="wood" x="306" y="0" width="304" height="160"/>
    <rect class="wood" x="170" y="157" width="568" height="140"/>
    <rect class="wood" x="0" y="295" width="740" height="220"/>
    <rect class="wood" x="718" y="270" width="250" height="245"/>
    <rect class="wood" x="963" y="155" width="237" height="500"/>
    <rect class="wood" x="170" y="510" width="568" height="140"/>
    <rect class="wood" x="306" y="648" width="304" height="157"/>
  </g>

  <g class="cut-lines">
    <path class="cut" d="M322 160 V24 H400 l6 -6 h22 l6 6 H582 V160"/>
    <path class="cut" d="M320 160 H190 V172 H320"/>
    <path class="cut" d="M190 172 V298 M583 172 H712 V298 H583"/>
    <path class="cut" d="M190 298 V310 H62 V380 H40 q-6 0 -6 6 V420 q0 6 6 6 H62 V497 H190 V510"/>
    <path class="cut" d="M190 510 V638 H320 M583 510 V638 H712 V510"/>
    <path class="cut" d="M320 650 V786 H400 l6 6 h22 l6 -6 H582 V650"/>
    <path class="cut" d="M712 298 H985 M718 515 H985 M712 510 H718"/>
    <path class="cut" d="M985 298 V175 Q1060 160 1100 240 Q1118 290 1115 390 Q1118 520 1070 600 Q1030 640 985 625 V515"/>
    <path class="cut" d="M1115 390 h-6 v20 h6"/>
    <rect class="cut" x="408" y="298" width="88" height="10" rx="5"/>
    <rect class="cut" x="408" y="500" width="88" height="10" rx="5"/>
    <rect class="cut" x="314" y="388" width="8" height="24" rx="3"/>
    <rect class="cut" x="322" y="456" width="8" height="18" rx="3"/>
  </g>

  <g class="crease-lines">
    <path class="crease" d="M320 168 H583"/>
    <path class="crease" d="M190 298 H720 M190 510 H720"/>
    <path class="crease" d="M190 305 V500 M320 298 V510 M583 298 V510 M718 298 V515"/>
    <path class="crease" d="M985 298 V515"/>
    <path class="crease" d="M320 648 H583"/>
    <path class="crease" d="M62 392 V414"/>
  </g>

  <g class="brand-lockup" transform="translate(452 236) rotate(180)">
    <text class="brand-name" x="0" y="0">PIKEMOOR</text>
    <text class="brand-tag" x="0" y="14">LOOK·TOUCH·PICK</text>
  </g>
  <g class="brand-lockup" transform="translate(256 408) rotate(90)">
    <text class="brand-name" x="0" y="0">PIKEMOOR</text>
    <text class="brand-tag" x="0" y="14">LOOK·TOUCH·PICK</text>
  </g>
  <g class="brand-lockup" transform="translate(640 404) rotate(90)">
    <text class="brand-name" x="0" y="0">PIKEMOOR</text>
    <text class="brand-tag" x="0" y="14">LOOK·TOUCH·PICK</text>
  </g>
  <g class="brand-lockup" transform="translate(856 400) rotate(-90)">
    <text class="brand-name" x="0" y="0">PIKEMOOR</text>
    <text class="brand-tag" x="0" y="14">LOOK·TOUCH·PICK</text>
  </g>
  <g class="brand-lockup" transform="translate(452 578)">
    <text class="brand-name" x="0" y="0">PIKEMOOR</text>
    <text class="brand-tag" x="0" y="14">LOOK·TOUCH·PICK</text>
  </g>

  <g class="insert-surface" role="img" aria-label="Grey wood plank photograph on the inside flap">
    <rect class="wood" x="313" y="840" width="295" height="440"/>
  </g>
  <g class="insert-cuts">
    <path class="cut" d="M357 870 H438 l6 6 h22 l6 -6 H565"/>
    <path class="cut" d="M357 870 Q290 862 250 900 Q225 930 235 960 Q245 990 300 995 Q330 998 357 998"/>
    <path class="cut" d="M565 870 Q632 862 672 900 Q697 930 687 960 Q677 990 622 995 Q592 998 565 998"/>
    <path class="cut" d="M357 998 V1262 H565 V998"/>
    <path class="crease" d="M357 998 H565 M357 870 V998 M565 870 V998"/>
  </g>

  <g class="insert-label">
    <rect class="label-panel" x="380" y="880" width="160" height="110" rx="4"/>
    <text class="brand-name label-name" x="458" y="917">PIKEMOOR</text>
    <text class="brand-tag label-tag" x="458" y="928">LOOK·TOUCH·PICK</text>
    <text class="label-caption" x="455" y="942">FLOORING SAMPLE SET</text>
    <path class="spec-rule" d="M410 950 h4 M410 955 h4 M410 960 h4 M410 965 h4"/>
  </g>

  <g class="spec-sheet">
    <rect class="label-panel" x="380" y="1012" width="160" height="230" rx="8"/>
    <rect class="spec-rule" x="396" y="1025" width="128" height="205" rx="5"/>
    <path class="spec-rule" d="M396 1040 H524 M396 1052 H524 M396 1064 H524 M396 1076 H524 M396 1088 H524 M396 1100 H524 M396 1112 H524 M396 1124 H524 M396 1136 H524 M396 1148 H524 M396 1160 H524 M396 1172 H524"/>
    <path class="spec-rule" d="M428 1025 V1172"/>
  </g>
</svg>
</body>
</html>
```